Letterhead and Envelopes design using existing logo. Logo can be found at tqvanholt.com

Use existing logo (attached) and incorporate in letterhead and envelope designs.

Current logo can be viewed at tqvanholt.com the web site reflect various parent and sub companies. Please see attached as well.

Target Market(s)

Other oil and gas operators.

Industry/Entity Type

Oil And Gas

Font styles to use
Sans Serif

Colors

Designer to choose colors to be used in the design.

Requirements
Must have
• Current logo and address
Nice to have
• Modern, contemporary approach yet incorporate existing traditional design.
• After design is selected for Wexford Tiller Holdings I will use similar design for Royalties, Exploration, Energy and Farms with different color schemes.

```html
<!DOCTYPE html>
<html lang="en">
<head>
<meta charset="utf-8">
<title>Wexford Tiller Holdings — Letterhead and Business Cards</title>
<link href="https://fonts.googleapis.com/css2?family=Arimo:wght@400;700&display=swap" rel="stylesheet">
<style>
  :root {
    --green: #5c9a35;
    --ink: #231f20;
    --paper: #ffffff;
    --card-grey: #ececec;
    --stage-dark: #25282c;
    --stage-light: #32363b;
    --text: #1f1f1f;
    --muted: #555555;
  }
  * { margin: 0; padding: 0; box-sizing: border-box; }
  html, body { width: 1200px; height: 866px; overflow: hidden; }
  body {
    position: relative;
    font-family: "Arimo", Arial, sans-serif;
    background: linear-gradient(115deg, var(--stage-dark) 0%, var(--stage-light) 55%, var(--stage-dark) 56%, #2c2f34 100%);
  }

  /* Letterhead */
  .letterhead {
    position: absolute; left: 37px; top: 20px;
    width: 579px; height: 846px;
    background: var(--paper);
    overflow: hidden;
  }
  .letterhead .frame { position: absolute; inset: 0; }
  .brand {
    position: absolute; left: 52px; top: 100px;
    display: flex; align-items: center; gap: 12px;
  }
  .brand-dot {
    width: 40px; height: 40px; border-radius: 50%;
    border: 3px solid var(--ink); flex: none;
  }
  .brand-name {
    font-size: 17px; font-weight: 700; line-height: 1.2; color: var(--ink);
  }
  .contact {
    position: absolute; right: 36px; top: 38px;
    list-style: none;
  }
  .contact li {
    display: flex; justify-content: flex-end; align-items: center;
    gap: 14px; height: 30.5px;
    font-size: 14px; color: var(--text);
  }
  .contact svg { width: 16px; height: 16px; fill: var(--green); flex: none; }
  .tagline {
    position: absolute; left: 39px; top: 241px;
    font-size: 16px; font-weight: 700; color: var(--text);
  }
  .body-copy {
    position: absolute; left: 48px; top: 278px;
    width: 475px; height: 416px; overflow: hidden;
    font-size: 13.6px; line-height: 17.3px; text-align: justify;
    color: var(--text);
  }
  .signature {
    position: absolute; left: 446px; top: 740px;
    font-size: 13px; font-weight: 700; color: var(--muted);
  }

  /* Business cards */
  .card {
    position: absolute; left: 711px; width: 421px; height: 233px;
    overflow: hidden;
  }
  .card .shapes { position: absolute; inset: 0; width: 100%; height: 100%; }
  .card-front { top: 25px; background: var(--card-grey); }
  .card-back { top: 283px; background: var(--ink); }
  .card-brand {
    position: absolute; left: 60px; top: 124px;
    display: flex; align-items: center; gap: 8px;
  }
  .card-brand .brand-dot { width: 26px; height: 26px; border-width: 2px; }
  .card-brand .brand-name { font-size: 12px; }
  .card-name {
    position: absolute; right: 38px; top: 36px;
    font-size: 24px; color: #ffffff;
  }
  .card-details {
    position: absolute; left: 36px; top: 168px;
    font-size: 15px; line-height: 30px; color: #ffffff;
  }
</style>
</head>
<body>

<article class="letterhead">
  <svg class="frame" viewBox="0 0 579 846" aria-hidden="true">
    <path d="M0,25 H296 Q309,25 309,38 V132" fill="none" stroke="var(--green)" stroke-width="18"/>
    <path d="M266,70 V158 Q266,169 277,169 H579" fill="none" stroke="var(--ink)" stroke-width="20" stroke-linecap="round"/>
    <path d="M0,761 H398 Q410,761 410,773 V846" fill="none" stroke="var(--ink)" stroke-width="18"/>
  </svg>

  <div class="brand">
    <span class="brand-dot"></span>
    <span class="brand-name">Wexford Tiller<br>Holdings</span>
  </div>

  <ul class="contact">
    <li>0123 Zip,abc City USA
      <svg viewBox="0 0 16 16"><path d="M8 1a5 5 0 0 0-5 5c0 4 5 9 5 9s5-5 5-9a5 5 0 0 0-5-5zm0 7a2 2 0 1 1 0-4 2 2 0 0 1 0 4z"/></svg></li>
    <li>+00 1234 56 789
      <svg viewBox="0 0 16 16"><path d="M3 1.5l3 .5 1 3-1.7 1.2a9 9 0 0 0 4.5 4.5L11 9l3 1 .5 3-2 1.5C7 14 2 9 1.5 3.5z"/></svg></li>
    <li>info@tqvanholt.com
      <svg viewBox="0 0 16 16"><path d="M15 1L1 7l5 2 1 5 2.5-3.5L13 13z"/></svg></li>
    <li>www.tqvanholt.com
      <svg viewBox="0 0 16 16"><circle cx="8" cy="8" r="7"/><path d="M6 4l5 4-5 4z" fill="#fff"/></svg></li>
  </ul>

  <h1 class="tagline">oil and gas company</h1>

  <p class="body-copy">your text here your text here your text here your text here your text here your text here your text here your text here your text here your text here your text here your text here your text here your text here your text here your text here your text here your text here your text here your text here your text here your text here your text here your text here your text here your text here your text here your text here your text here your text here your text here your text here your text here your text here your text here your text here your text here your text here your text here your text here your text here your text here your text here your text here your text here your text here your text here your text here your text here your text here your text here your text here your text here your text here your text here your text here your text here your text here your text here your text here your text here your text here your text here your text here your text here your text here your text here your text here your text here your text here your text here your text here your text here your text here your text here your text here your text here your text here your text here your text here your text here your text here your text here your text here your text here your text here your text here your text here your text here your text here your text here your text here your text here your text here your text here your text here your text here your text here your text here your text here your text here your text here your text here your text here your text here your text here your text here your text here your text here your text here your text here your text here your text here your text here your text here your text here your text here your text here your text here your text here your text here your text here your text here your text here your text here your text here your text here your text here your text here your text here your text here your text here your text here your text here your text here your text here your text here your text here your text here your text here your text here your text here your text here your text here your text here your text here your text here your text here your text here your text here your text here your text here your text here your text here your text here your text here your text here your text here</p>

  <p class="signature">Signature</p>
</article>

<section class="card card-front">
  <svg class="shapes" viewBox="0 0 248 137" preserveAspectRatio="none" aria-hidden="true">
    <path d="M0,0 H248 V70 C160,40 70,40 0,56 Z" fill="var(--ink)"/>
    <path d="M60,0 H248 V92 C170,94 105,62 60,0 Z" fill="var(--green)"/>
    <path d="M248,92 C170,94 105,62 60,0" fill="none" stroke="#ffffff" stroke-width="2.5"/>
    <path d="M0,56 C70,40 160,40 248,70" fill="none" stroke="#ffffff" stroke-width="1.5"/>
  </svg>
  <div class="card-brand">
    <span class="brand-dot"></span>
    <span class="brand-name">Wexford Tiller<br>Holdings</span>
  </div>
</section>

<section class="card card-back">
  <svg class="shapes" viewBox="0 0 248 136" preserveAspectRatio="none" aria-hidden="true">
    <path d="M0,0 H248 V40 C160,38 70,38 0,54 Z" fill="var(--card-grey)"/>
    <path d="M0,54 C70,38 160,38 248,40" fill="none" stroke="#ffffff" stroke-width="2"/>
    <path d="M60,0 H248 V88 C170,90 105,60 60,0 Z" fill="var(--green)"/>
    <path d="M248,88 C170,90 105,60 60,0" fill="none" stroke="#ffffff" stroke-width="2.5"/>
  </svg>
  <p class="card-name">Your Name</p>
  <p class="card-details">Your adress here 1234<br>Your phone 0234-5678 / www.tqvanholt.com</p>
</section>

</body>
</html>
```